Software Company Business Card

We are looking for a new design of our business card. The design will also be used in the rest of our branding and marketing materials as we want to keep it all uniform. We sell POS software to fine/luxury jewelers and also offer other business services as well to help the jeweler manage their business and need something more updated, technical and fresh, preferably more on the masculine side. We do not want any designs with gems in them but if possible would like to incorporate the circle and arrow in the logo into the design, but not a requirement if you can't make it work. I would like to see a variety of the mix. The colors need to remain our blue and orange and the logo can not change. The squiggly lines have been used as our corporate identity for over 20 years and its time to update. Our company name is PELK (Bright Ledger Counter Solutions).

Target Market(s)

High End Jewelers

Industry/Entity Type

Software

Contact Information for Business Card

Requirements
Must have
• Our logo and the colors must remain the same. Blue is #d95d39 and Orange is #0f5682.
Nice to have
• The circle and arrow incorporated but not a requirement.
Should not have
• Anything jewelry or gem related.

```html
<!DOCTYPE html>
<html lang="en">
<head>
<meta charset="utf-8">
<title>PELK Business Card</title>
<link rel="stylesheet" href="https://fonts.googleapis.com/css2?family=Montserrat:wght@500;600;700;800&display=swap">
<style>
  :root {
    --brand-blue: #0d4fa8;
    --brand-red: #e03a25;
    --ink: #111111;
    --paper: #ffffff;
    --night: #000000;
    --ghost-light: #f2f2f2;
    --ghost-dark: #0f0f0f;
  }
  * { margin: 0; padding: 0; box-sizing: border-box; }
  html, body {
    width: 1200px; height: 1000px; overflow: hidden;
    background: var(--paper);
    font-family: "Montserrat", sans-serif;
  }
  .card {
    position: absolute; left: 244px;
    width: 712px; height: 407px; overflow: hidden;
  }
  .card--front { top: 70px; background: var(--paper); box-shadow: 3px 4px 8px rgba(0,0,0,0.35); }
  .card--back { top: 524px; background: var(--night); }
  .backdrop-disc { position: absolute; left: 0; top: 0; }
  .wordmark {
    position: absolute; font-weight: 800; color: var(--brand-blue);
    letter-spacing: 1px; line-height: 1;
  }
  .card--front .wordmark { left: 51px; top: 50px; font-size: 50px; }
  .card--back .wordmark { left: 51px; top: 172px; font-size: 62px; }
  .dot { position: absolute; }
  .holder {
    position: absolute; left: 0; width: 712px; text-align: center;
  }
  .holder__name { top: 205px; font-size: 27px; font-weight: 700; color: var(--brand-blue); letter-spacing: 0.3px; }
  .holder__title { top: 242px; font-size: 19.5px; font-weight: 500; color: var(--brand-red); }
  .rule { position: absolute; left: 0; top: 0; }
  .contact {
    position: absolute; left: 0; top: 286px; width: 712px;
    text-align: center; font-size: 20px; font-weight: 500; color: var(--ink); line-height: 24px;
  }
  .address {
    position: absolute; left: 407px; top: 146px;
    color: var(--brand-red); font-size: 19px; font-weight: 500; line-height: 22px;
  }
  .address__web { margin-top: 24px; font-weight: 700; font-size: 19.5px; }
</style>
</head>
<body>
  <section class="card card--front">
    <svg class="backdrop-disc" width="712" height="407" aria-hidden="true">
      <circle cx="356" cy="203" r="254" fill="var(--ghost-light)"/>
    </svg>
    <div class="wordmark">PELK</div>
    <svg class="dot" style="left:206px;top:50px" width="54" height="54" aria-hidden="true">
      <circle cx="27" cy="27" r="25" fill="var(--brand-red)"/>
    </svg>
    <div class="holder holder__name">DECLAN HARWICK</div>
    <div class="holder holder__title">Director of Global Operations</div>
    <svg class="rule" width="712" height="407" aria-hidden="true">
      <rect x="51" y="271" width="560" height="7" rx="3.5" fill="var(--brand-red)"/>
      <circle cx="626" cy="257" r="35" fill="var(--brand-red)"/>
    </svg>
    <div class="contact">
      <p>Phone: +1 800 555-0142</p>
      <p>Fax: +1 702 555-0187</p>
      <p>Email: declan@pelkusa.com</p>
    </div>
  </section>

  <section class="card card--back">
    <svg class="backdrop-disc" width="712" height="407" aria-hidden="true">
      <circle cx="356" cy="203" r="254" fill="var(--ghost-dark)"/>
    </svg>
    <div class="wordmark">PELK</div>
    <svg class="dot" style="left:246px;top:168px" width="70" height="70" aria-hidden="true">
      <circle cx="35" cy="35" r="34" fill="var(--brand-red)"/>
    </svg>
    <div class="address">
      <p>1480 Summit Ridge Drive</p>
      <p>Suite 210</p>
      <p>Carson Vale, NV 89512 USA</p>
      <p class="address__web">www.pelkusa.com</p>
    </div>
  </section>
</body>
</html>
```